Fern Pantry needs a bottle label design

We need a bottle label design that is clean, simple and fun. The labels will be for different drink products; OAT. MILK. ALMOND MILK. SOY. We imagine our FP logo at the top, then our brand name FERN PANTRY to be positioned above the the product type OAT. MILK. ALMOND MILK. SOY etc. Underneath the product is made in new zealand. At the base is a check box (suggest using hearts) to denote vegan, planet, dairy free, and recycle friendly. At bottom is bottle size eg 1L, 380ml, 250ml. These are the 3 bottle sizes. Our logo is neon green on light grey background. Fern PAntry is white. back label info to be supplied. Sleeve is under the cap and should have a solid colour around neck. Sleeve to be on white background.

Target Market(s)

25-40 - skew female

Font styles to use
Sans Serif

Requirements
Must have
• Fp Logo and fern pantry
Red hearts against the checks: vegan, recycle, dairy free, planet claims
We are using white caps
The sleeve is going from base to under top of the neck of bottle but will not cover the made in New Zealand underneath the product type eg OAT

```html
<!DOCTYPE html>
<html lang="en">
<head>
<meta charset="utf-8">
<title>Fern Pantry Oat Milk Label</title>
<link rel="stylesheet" href="https://fonts.googleapis.com/css2?family=Fredoka:wght@600&family=Roboto+Condensed:wght@400&family=Montserrat:wght@700&display=swap">
<style>
  :root {
    --bg: #ececec;
    --oat-brown: #b5662b;
    --oat-brown-light: #c47a3c;
    --logo-grey: #6d6e70;
    --neon-green: #5cc63a;
    --white: #ffffff;
    --heart-red: #e0443a;
    --claim-brown: #b5662b;
  }
  html, body {
    margin: 0;
    padding: 0;
    width: 1200px;
    height: 1200px;
    overflow: hidden;
    background: linear-gradient(180deg, #dedede 0%, #f6f6f6 100%);
  }
  .canvas {
    position: relative;
    width: 1200px;
    height: 1200px;
  }
  .label {
    position: absolute;
    left: 300px;
    top: 60px;
    width: 600px;
    height: 1080px;
    background: var(--white);
    border-radius: 24px;
    overflow: hidden;
    box-shadow: 0 6px 24px rgba(0,0,0,0.08);
  }
  .label-colour-band {
    position: absolute;
    inset: 0 0 auto 0;
    height: 700px;
    background: linear-gradient(180deg, var(--oat-brown) 0%, var(--oat-brown-light) 100%);
  }
  .brand-tab {
    position: absolute;
    left: 150px;
    top: 30px;
    width: 300px;
    height: 170px;
    background: var(--logo-grey);
    border-radius: 70px 70px 70px 10px;
    display: flex;
    flex-direction: column;
    align-items: center;
    justify-content: center;
    gap: 12px;
  }
  .brand-mark {
    display: flex;
    align-items: center;
    gap: 12px;
  }
  .brand-dot {
    width: 22px;
    height: 22px;
    border-radius: 50%;
    background: var(--neon-green);
  }
  .brand-initials {
    font-family: "Montserrat", sans-serif;
    font-weight: 700;
    font-size: 76px;
    line-height: 1;
    color: var(--neon-green);
  }
  .brand-name {
    font-family: "Montserrat", sans-serif;
    font-weight: 700;
    font-size: 20px;
    letter-spacing: 4px;
    color: var(--white);
  }
  .product-name {
    position: absolute;
    left: 0;
    right: 0;
    top: 215px;
    margin: 0;
    text-align: center;
    font-family: "Fredoka", sans-serif;
    font-weight: 600;
    color: var(--white);
    line-height: 0.95;
  }
  .product-name .line-oat { display: block; font-size: 180px; letter-spacing: 8px; }
  .product-name .line-milk { display: block; font-size: 150px; letter-spacing: 6px; }
  .origin {
    position: absolute;
    left: 0;
    right: 0;
    top: 560px;
    text-align: center;
    font-family: "Roboto Condensed", sans-serif;
    font-size: 34px;
    letter-spacing: 1px;
    color: var(--white);
  }
  .splash-art {
    position: absolute;
    left: 0;
    right: 0;
    top: 630px;
    height: 380px;
    background: linear-gradient(180deg, rgba(255,255,255,0) 0%, #f7f2ea 30%, #e9cf9c 65%, #ffffff 100%);
  }
  .claims {
    position: absolute;
    left: 40px;
    top: 920px;
    margin: 0;
    padding: 0;
    list-style: none;
    font-family: "Roboto Condensed", sans-serif;
    font-size: 20px;
    color: var(--claim-brown);
  }
  .claims li {
    display: flex;
    align-items: center;
    gap: 10px;
    height: 30px;
  }
  .claims svg { width: 20px; height: 18px; }
  .volume {
    position: absolute;
    right: 40px;
    top: 990px;
    font-family: "Roboto Condensed", sans-serif;
    font-size: 34px;
    color: var(--claim-brown);
  }
</style>
</head>
<body>
<main class="canvas">
  <section class="label">
    <div class="label-colour-band"></div>

    <div class="brand-tab">
      <div class="brand-mark">
        <span class="brand-dot"></span>
        <span class="brand-initials">FP</span>
      </div>
      <span class="brand-name">FERN PANTRY</span>
    </div>

    <h1 class="product-name">
      <span class="line-oat">OAT</span>
      <span class="line-milk">MILK</span>
    </h1>
    <div class="origin">MADE IN NEW ZEALAND</div>

    <div class="splash-art" role="img" aria-label="Illustration of a milk splash with oat stalks, a wooden scoop of oats and a bowl of porridge topped with strawberries"></div>

    <ul class="claims">
      <li><svg viewBox="0 0 20 18"><path d="M10 16 L2.5 8.5 A4 4 0 0 1 10 4 A4 4 0 0 1 17.5 8.5 Z" fill="none" stroke="var(--heart-red)" stroke-width="2"/><path d="M6 9 L9 12 L15 5" fill="none" stroke="var(--heart-red)" stroke-width="1.6"/></svg>VEGAN</li>
      <li><svg viewBox="0 0 20 18"><path d="M10 16 L2.5 8.5 A4 4 0 0 1 10 4 A4 4 0 0 1 17.5 8.5 Z" fill="none" stroke="var(--heart-red)" stroke-width="2"/><path d="M6 9 L9 12 L15 5" fill="none" stroke="var(--heart-red)" stroke-width="1.6"/></svg>RECYCLE</li>
      <li><svg viewBox="0 0 20 18"><path d="M10 16 L2.5 8.5 A4 4 0 0 1 10 4 A4 4 0 0 1 17.5 8.5 Z" fill="none" stroke="var(--heart-red)" stroke-width="2"/><path d="M6 9 L9 12 L15 5" fill="none" stroke="var(--heart-red)" stroke-width="1.6"/></svg>DAIRY FREE</li>
      <li><svg viewBox="0 0 20 18"><path d="M10 16 L2.5 8.5 A4 4 0 0 1 10 4 A4 4 0 0 1 17.5 8.5 Z" fill="none" stroke="var(--heart-red)" stroke-width="2"/><path d="M6 9 L9 12 L15 5" fill="none" stroke="var(--heart-red)" stroke-width="1.6"/></svg>PLANET CLAIMS</li>
    </ul>

    <div class="volume">Net Wt. 250ml</div>
  </section>
</main>
</body>
</html>
```